Business Card Design - Carrington Hill Lodge

We are looking at a new design for our business cards that has a modern and professional look. We run a residential aged care facility focussing on the care of residents. The cards will be used for potential clients, consultants and business opportunities in this sector. Blue and white is our main colours and would to see these colours incorporated in the design.
Industry/Entity Type
Business
Contact Information for Business Card
Carrington Hill Lodge, Darren Pelham, dpelham@carringtonhilllodge.com.au, Finance Manager, 0491 736 208, BCom, 48 Yarrabee Way, Kelvin Ridge, Qld 4135.

```html
<!DOCTYPE html>
<html lang="en">
<head>
<meta charset="utf-8">
<title>Carrington Hill Lodge – Business Card</title>
<link href="https://fonts.googleapis.com/css2?family=Arimo:wght@400;700&display=swap" rel="stylesheet">
<style>
  :root {
    --stage: #2e2e2e;
    --card-white: #ffffff;
    --card-shade: #e9eaeb;
    --brand-blue: #42667f;
    --brand-blue-light: #5b7f98;
    --swoosh-dark: #3a3a3c;
    --ink-dark: #333335;
    --ink-light: #ffffff;
  }
  html, body {
    margin: 0;
    width: 1200px;
    height: 997px;
    overflow: hidden;
    background: var(--stage);
    font-family: "Arimo", Arial, sans-serif;
  }
  .card {
    position: absolute;
    left: 290px;
    width: 620px;
    height: 354px;
    border-radius: 18px;
    overflow: hidden;
    background: linear-gradient(135deg, var(--card-white) 40%, var(--card-shade));
  }
  .card--front { top: 114px; }
  .card--back { top: 528px; }
  .card__shapes { position: absolute; inset: 0; }

  .brand {
    position: absolute;
    display: flex;
    align-items: center;
    gap: 12px;
  }
  .brand__dot {
    border-radius: 50%;
    background: var(--brand-blue-light);
    flex: none;
  }
  .brand__name {
    color: var(--brand-blue);
    font-weight: 400;
    text-transform: uppercase;
    letter-spacing: 0.08em;
    white-space: nowrap;
  }
  .card--front .brand { left: 70px; top: 128px; }
  .card--front .brand__dot { width: 44px; height: 44px; }
  .card--front .brand__name { font-size: 24px; }
  .card--back .brand { right: 26px; top: 58px; }
  .card--back .brand__dot { width: 30px; height: 30px; }
  .card--back .brand__name { font-size: 17px; }

  .website {
    position: absolute;
    right: 22px;
    bottom: 20px;
    color: var(--ink-light);
    font-size: 13px;
    letter-spacing: 0.02em;
  }

  .holder { position: absolute; left: 30px; top: 96px; }
  .holder__name {
    margin: 0;
    color: var(--brand-blue);
    font-weight: 700;
    font-size: 27px;
    font-variant: small-caps;
    letter-spacing: 0.02em;
    line-height: 1;
  }
  .holder__role {
    margin: 2px 0 0;
    color: var(--ink-dark);
    font-size: 17px;
    font-variant: small-caps;
    letter-spacing: 0.03em;
  }

  .contacts {
    position: absolute;
    left: 22px;
    top: 256px;
    margin: 0;
    padding: 0;
    list-style: none;
  }
  .contacts__item {
    display: flex;
    align-items: center;
    gap: 12px;
    height: 28px;
    color: var(--ink-light);
    font-size: 15px;
    letter-spacing: 0.02em;
  }
  .contacts__icon { width: 16px; height: 16px; flex: none; }
</style>
</head>
<body>

<section class="card card--front" aria-label="Card front">
  <svg class="card__shapes" viewBox="0 0 620 354" aria-hidden="true">
    <path d="M180 354 C400 330 560 262 620 168 L620 196 C562 276 410 340 205 354 Z" fill="var(--swoosh-dark)"/>
    <path d="M205 354 C410 340 562 276 620 196 L620 354 Z" fill="var(--brand-blue)"/>
  </svg>
  <div class="brand">
    <span class="brand__dot"></span>
    <span class="brand__name">Carrington Hill Lodge</span>
  </div>
  <span class="website">www.carringtonhilllodge.com.au</span>
</section>

<section class="card card--back" aria-label="Card back">
  <svg class="card__shapes" viewBox="0 0 620 354" aria-hidden="true">
    <path d="M0 196 C220 150 440 150 580 182 L620 194 L620 354 L0 354 Z" fill="var(--swoosh-dark)"/>
    <path d="M0 224 C220 180 460 170 620 198 L620 354 L0 354 Z" fill="var(--brand-blue)"/>
  </svg>

  <div class="holder">
    <h1 class="holder__name">Darren Pelham</h1>
    <p class="holder__role">Finance Manager</p>
  </div>

  <div class="brand">
    <span class="brand__dot"></span>
    <span class="brand__name">Carrington Hill Lodge</span>
  </div>

  <ul class="contacts">
    <li class="contacts__item">
      <svg class="contacts__icon" viewBox="0 0 16 16" aria-hidden="true">
        <rect x="0" y="0" width="16" height="16" rx="3" fill="#fff"/>
        <rect x="5" y="3" width="6" height="10" rx="1" fill="none" stroke="var(--brand-blue)" stroke-width="1.4"/>
      </svg>
      <span>0491 736 208</span>
    </li>
    <li class="contacts__item">
      <svg class="contacts__icon" viewBox="0 0 16 16" aria-hidden="true">
        <rect x="0" y="0" width="16" height="16" rx="3" fill="#fff"/>
        <rect x="3" y="5" width="10" height="7" fill="none" stroke="var(--brand-blue)" stroke-width="1.3"/>
        <path d="M3 5 L8 9 L13 5" fill="none" stroke="var(--brand-blue)" stroke-width="1.3"/>
      </svg>
      <span>dpelham@carringtonhilllodge.com.au</span>
    </li>
    <li class="contacts__item">
      <svg class="contacts__icon" viewBox="0 0 16 16" aria-hidden="true">
        <rect x="0" y="0" width="16" height="16" rx="3" fill="#fff"/>
        <path d="M8 13 C5 9.5 4.5 8 4.5 6.5 A3.5 3.5 0 0 1 11.5 6.5 C11.5 8 11 9.5 8 13 Z" fill="var(--brand-blue)"/>
        <circle cx="8" cy="6.5" r="1.3" fill="#fff"/>
      </svg>
      <span>48 Yarrabee Way, Kelvin Ridge, Qld 4135</span>
    </li>
  </ul>
</section>

</body>
</html>
```